Bar Wanderlight VIP Card design

Looking for a design for a VIP card forguests wishing to purchase to avoid cover charges, skipping the line and othe advantages.

We used our logo on last years card.I've also attached a few of our previous cards. Looking for something fresh.

We are not apposed to a vertical card either way would be fine We will have to incorporate the fizz mild logo on the card as well.

Industry/Entity Type

Bar Restaurant www.bar-w.example

Font styles to use
Decorative

```html
<!DOCTYPE html>
<html lang="en">
<head>
<meta charset="utf-8">
<title>Bar Wanderlight VIP Card</title>
<link rel="stylesheet" href="https://fonts.googleapis.com/css2?family=Cinzel:wght@700&family=Oswald:wght@700&display=swap">
<style>
  :root {
    --stage: #2b2b2d;
    --card-violet: #3d1a86;
    --band-violet: #2e0f5a;
    --gold-light: #fbf0a0;
    --gold-mid: #d9b12a;
    --gold-deep: #a9800f;
    --name-yellow: #f3e36b;
  }
  html, body {
    margin: 0;
    padding: 0;
    width: 1200px;
    height: 800px;
    overflow: hidden;
    background: var(--stage);
  }
  .canvas {
    position: relative;
    width: 1200px;
    height: 800px;
  }
  .vip-card {
    position: absolute;
    left: 120px;
    top: 97px;
    width: 960px;
    height: 605px;
    border-radius: 24px;
    background: var(--card-violet);
    overflow: hidden;
  }
  .brand-name {
    position: absolute;
    left: 0;
    right: 0;
    top: 140px;
    margin: 0;
    text-align: center;
    font-family: "Cinzel", serif;
    font-weight: 700;
    font-size: 54px;
    letter-spacing: 1px;
    color: var(--name-yellow);
  }
  .gold-rule {
    position: absolute;
    left: 0;
    width: 100%;
    height: 8px;
    background: linear-gradient(90deg, var(--gold-deep), var(--gold-light) 30%, var(--gold-mid) 60%, var(--gold-light) 85%, var(--gold-deep));
  }
  .gold-rule--top { top: 380px; }
  .gold-rule--bottom { top: 540px; }
  .tier-band {
    position: absolute;
    left: 0;
    top: 388px;
    width: 100%;
    height: 152px;
    background: var(--band-violet);
    display: flex;
    align-items: center;
    justify-content: center;
  }
  .tier-label {
    margin: 0;
    font-family: "Oswald", sans-serif;
    font-weight: 700;
    font-size: 172px;
    line-height: 1;
    letter-spacing: -2px;
    background: linear-gradient(100deg, var(--gold-deep) 0%, var(--gold-light) 30%, var(--gold-mid) 55%, var(--gold-light) 75%, var(--gold-deep) 100%);
    -webkit-background-clip: text;
    background-clip: text;
    color: transparent;
    transform: scaleY(0.85);
  }
</style>
</head>
<body>
  <main class="canvas">
    <section class="vip-card">
      <h1 class="brand-name">Bar Wanderlight</h1>
      <div class="gold-rule gold-rule--top"></div>
      <div class="tier-band">
        <p class="tier-label">VIP</p>
      </div>
      <div class="gold-rule gold-rule--bottom"></div>
    </section>
  </main>
</body>
</html>
```